Company Stationary, Business Card, Enevelopes, Letterhead
Would also like note stationary, and enevelope to fit
Company Stationary, Business Card, Enevelopes, Letterhead - Real Estate
Creative Brief
Professional
Dale Harwick
Designated Broker/Owner
2716 Juniper Loop Ste 214 Harlow Springs, NV. 99417
dale@brightfieldhomepartners.net
www.brightfieldhomepartners.net

```html
<!DOCTYPE html>
<html lang="en">
<head>
<meta charset="utf-8">
<title>Brightfield Home Partners – Business Card</title>
<link rel="stylesheet" href="https://fonts.googleapis.com/css2?family=Cinzel:wght@400;700&family=Cormorant+Garamond:wght@500&display=swap">
<style>
  :root {
    --brand-red: #c4161c;
    --deep-red: #8e0f14;
    --charcoal: #3a3a3a;
    --mid-grey: #7a7a7a;
    --paper: #ffffff;
    --backdrop: #ececec;
  }
  * { box-sizing: border-box; margin: 0; padding: 0; }
  html, body { width: 1200px; height: 1006px; overflow: hidden; }
  body {
    background: var(--backdrop);
    font-family: "Cormorant Garamond", Georgia, serif;
    color: var(--charcoal);
    position: relative;
  }
  .card {
    position: absolute;
    left: 190px;
    width: 820px;
    height: 469px;
    background: var(--paper);
    border-radius: 22px;
    overflow: hidden;
    box-shadow: 0 4px 14px rgba(0,0,0,0.12);
  }
  .card--front { top: 22px; }
  .card--back { top: 515px; }

  .brand {
    display: flex;
    align-items: center;
    gap: 16px;
  }
  .brand__dot {
    width: 54px; height: 54px;
    border-radius: 50%;
    background: var(--brand-red);
    flex: none;
  }
  .brand__name {
    font-family: "Cinzel", Georgia, serif;
    font-weight: 700;
    color: var(--brand-red);
    font-size: 34px;
    letter-spacing: 1px;
    line-height: 1;
  }
  .card--front .brand { position: absolute; left: 44px; top: 48px; }

  .contact {
    position: absolute;
    left: 46px; top: 140px;
    list-style: none;
    font-size: 17px;
    line-height: 1.5;
    color: var(--charcoal);
  }

  .swoosh { position: absolute; left: 0; bottom: 0; width: 820px; height: 469px; }

  .web {
    position: absolute;
    left: 0; right: 0; bottom: 12px;
    text-align: center;
    font-family: "Cinzel", Georgia, serif;
    font-size: 14px;
    letter-spacing: 2px;
    color: var(--paper);
    text-transform: uppercase;
  }

  .agent {
    position: absolute;
    right: 48px; bottom: 70px;
    text-align: right;
  }
  .agent__name {
    font-family: "Cinzel", Georgia, serif;
    font-weight: 700;
    font-size: 24px;
    color: var(--brand-red);
    letter-spacing: 1px;
  }
  .agent__title {
    font-size: 17px;
    color: var(--mid-grey);
    letter-spacing: 1px;
    text-transform: uppercase;
  }

  .card--back .brand {
    position: absolute;
    left: 0; right: 0; top: 180px;
    justify-content: center;
  }
  .card--back .web-back {
    position: absolute;
    left: 0; right: 0; top: 272px;
    text-align: center;
    font-family: "Cinzel", Georgia, serif;
    font-size: 15px;
    letter-spacing: 3px;
    color: var(--charcoal);
    text-transform: uppercase;
  }
</style>
</head>
<body>

<section class="card card--front">
  <div class="brand">
    <span class="brand__dot"></span>
    <span class="brand__name">Brightfield Home Partners</span>
  </div>

  <ul class="contact">
    <li>2716 Juniper Loop Ste 214</li>
    <li>Harlow Springs, NV. 99417</li>
    <li>P 555.010.0142</li>
    <li>F 555.010.0187</li>
    <li>dale@brightfieldhomepartners.net</li>
    <li>marvendalegroup</li>
  </ul>

  <svg class="swoosh" viewBox="0 0 820 469" aria-hidden="true">
    <path d="M0 318 C150 322 240 392 380 420 L820 420 L820 469 L0 469 Z" fill="var(--charcoal)"/>
    <path d="M0 334 C140 338 230 404 370 430 L820 430 L820 469 L0 469 Z" fill="var(--brand-red)"/>
    <path d="M0 360 C130 366 220 420 360 446 L820 446 L820 469 L0 469 Z" fill="var(--deep-red)" opacity="0.35"/>
  </svg>

  <div class="agent">
    <div class="agent__name">Dale Harwick</div>
    <div class="agent__title">Designated Broker/Owner</div>
  </div>

  <div class="web">www.brightfieldhomepartners.net</div>
</section>

<section class="card card--back">
  <div class="brand">
    <span class="brand__dot"></span>
    <span class="brand__name">Brightfield Home Partners</span>
  </div>
  <div class="web-back">www.brightfieldhomepartners.net</div>
</section>

</body>
</html>
```